Etikettendesign für eine Grillsauce gesucht
Zielgruppe
Genuss aus dem Herzen der Schweiz
Kräuterbutter für Feinschmecker – dafür steht die Hubertsen’s Feinkost AG seit vielen Jahren. Mitten aus dem grünen Herzen der Schweiz verkündet die Hubertsen’s Feinkost AG ihre Genussbotschaft:
Der sorgsame Umgang mit den Rohstoffen der Natur ist die Grundlage für hochwertigen Genuss und vollmundigen Geschmack.
In jedem Produkt der Hubertsen’s Feinkost AG schmeckt man den Einklang mit der Natur: aromatisch, harmonisch, ausgewogen.
Aufgabenstellung
Eine neues Produkt soll entstehen.
- eine Grillsauce. Produktetikett für eine Flasche mit 500ml (welche noch nicht definiert ist) Es handelt sich hier um eine Lebensmitteletikette. Produktangaben wie Inhalte und Nährwerte werden auf dem Rücketikett stehen.
Wir brauchen das Designe für die Frontetikette.
Gestartet wird mit einer Sauce. Weitere Saucen sollen dann folgen.
- Lindo Sauce
- Chimichurri
- Café de Paris
- BBQ
Wir sind noch total in der Findung für ein neues Design. Was wir suchen ist ein Design welches sehr edel daher kommt und Lust auf mehr macht. Die Zielgruppe wird eher der Fleischkonsument und der Grillmeister sein.
Es darf im Vintage stil sein, soll aber elegant und edel wirken.
Es soll in Richtung Lifestyle Produkt gehen, welches der Metzger gerne in seinem Regal stehen hat oder das BBQ Restaurant auf den Tisch stellen will.
Eine Idee z.b. wäre, dass wir alle Saucen in die Roten Ketchup Quetflaschen abfüllen um ein alleinstellungsmerkmal zu haben.

```html
<!DOCTYPE html>
<html lang="de">
<head>
<meta charset="utf-8">
<title>Kräuterbutter für Feinschmecker – Etikett</title>
<link href="https://fonts.googleapis.com/css2?family=Lobster&family=Roboto:wght@400;500&display=swap" rel="stylesheet">
<style>
  :root {
    --stage: #f5f5f5;
    --paper: #ffffff;
    --cream: #efe9e1;
    --kraft: #d9b892;
    --kraft-dark: #c9a47c;
    --ink: #1d1a17;
    --body: #3b3430;
    --brand-red: #d8262b;
    --herb: #4f9a3c;
    --herb-dark: #2f7030;
  }
  * { box-sizing: border-box; margin: 0; padding: 0; }
  html, body { width: 1200px; height: 800px; overflow: hidden; }
  body {
    background: var(--stage);
    font-family: "Roboto", sans-serif;
    position: relative;
  }

  /* Neck label */
  .neck-label {
    position: absolute;
    left: 170px; top: 320px;
    width: 320px; height: 160px;
    background: var(--kraft);
    display: flex; align-items: center; justify-content: center;
    box-shadow: 0 6px 20px rgba(0,0,0,.08);
  }
  .brand-name {
    font-family: "Roboto", sans-serif;
    font-weight: 500;
    font-size: 22px;
    color: var(--brand-red);
    letter-spacing: .5px;
  }

  /* Front label */
  .front-label {
    position: absolute;
    left: 620px; top: 50px;
    width: 400px; height: 700px;
    background: var(--paper);
    overflow: hidden;
    box-shadow: 0 6px 24px rgba(0,0,0,.08);
  }
  .label-shapes { position: absolute; inset: 0; }
  .serving-scene {
    position: absolute;
    left: 0; top: 330px;
    width: 400px; height: 370px;
    background:
      radial-gradient(ellipse 60% 35% at 45% 70%, rgba(79,154,60,.35), transparent 70%),
      radial-gradient(ellipse 70% 50% at 35% 45%, rgba(255,255,255,.95), transparent 75%),
      linear-gradient(180deg, rgba(244,240,232,0) 0%, #f1ece3 45%, #f6f2ec 100%);
  }
  .title-block {
    position: absolute;
    left: 0; right: 0; top: 88px;
    text-align: center;
  }
  .title-main {
    font-family: "Lobster", cursive;
    font-size: 56px;
    line-height: 1;
    color: var(--ink);
    transform: rotate(-4deg);
  }
  .title-sub {
    font-family: "Lobster", cursive;
    font-size: 54px;
    line-height: 1;
    color: var(--paper);
    text-shadow: 2px 2px 0 var(--ink);
    transform: rotate(-4deg);
    margin-top: 4px;
    padding-left: 30px;
    position: relative;
  }
  .title-sub .for {
    position: absolute;
    left: 22px; top: -6px;
    font-size: 22px;
    text-shadow: 1px 1px 0 var(--ink);
  }
  .claim {
    position: absolute;
    left: 50px; right: 50px; top: 238px;
    font-size: 13.5px;
    line-height: 1.35;
    letter-spacing: .8px;
    color: var(--body);
    text-align: center;
    transform: rotate(-3deg);
  }
  .organic-seal {
    position: absolute;
    left: 268px; top: 420px;
    width: 110px; height: 110px;
  }
</style>
</head>
<body>

  <section class="neck-label" aria-label="Halsetikett">
    <span class="brand-name">Hubertsen’s Feinkost AG</span>
  </section>

  <section class="front-label" aria-label="Frontetikett">
    <svg class="label-shapes" viewBox="0 0 400 700" width="400" height="700" aria-hidden="true">
      <rect width="400" height="700" fill="var(--paper)"/>
      <path d="M0 40 C120 10 260 20 400 0 L400 110 C260 80 120 70 0 110 Z" fill="var(--cream)"/>
      <path d="M0 75 C110 35 270 55 400 25 L400 560 C320 520 230 560 150 540 C90 520 40 500 0 470 Z" fill="var(--kraft)"/>
    </svg>

    <div class="serving-scene" role="img" aria-label="Illustration: Kräuterbutter-Spritzer mit frischen Kräuterblättern in einer Schale"></div>

    <div class="title-block">
      <div class="title-main">Kräuterbutter</div>
      <div class="title-sub"><span class="for">für</span>Feinschmecker</div>
    </div>

    <p class="claim">The careful handling of natural raw materials is the basis for high-quality enjoyment and full-bodied taste.</p>

    <svg class="organic-seal" viewBox="0 0 110 110" aria-label="Bio-Siegel">
      <path d="M0 62 L110 40 L104 58 L6 80 Z" fill="var(--herb-dark)"/>
      <circle cx="55" cy="55" r="42" fill="var(--paper)" stroke="var(--herb)" stroke-width="4"/>
      <circle cx="55" cy="55" r="33" fill="var(--herb)"/>
    </svg>
  </section>

</body>
</html>
```